Business Card Design Project

We need a business card design for an existing company in Dallas/Fort Worth that is expanding services and re-branding. We are changing the name from Brightmoor Commercial Cleaning to Keystride Facility Services. We are expanding from only commercial cleaning to include complete commercial landscape and facility maintenance services, too.

As stated, we offer a package of services that includes landscape, janitorial and facility services, which is largely unique in the industry.

We would like a design that communicates trust/partnership with a professional, corporate image, but not necessarily using the standard white business card. We would like a design that perhaps uses darker blues or perhaps a gray background, but we are open to other ideas. We might also be interested in a double-sided design - maybe with our logo on the back, printed on a gray background?

We will probably stick with the attached logo, but if you've got another inspired idea....

Target Market(s)

Property managers, commercial real estate professionals, corporate executives

Industry/Entity Type

Landscape

Requirements
Should not have
• Not interested in old style fonts.

```html
<!DOCTYPE html>
<html lang="en">
<head>
<meta charset="utf-8">
<title>Keystride Facility Services – Business Card</title>
<link rel="stylesheet" href="https://fonts.googleapis.com/css2?family=Questrial&display=swap">
<style>
  :root {
    --page-bg: #4a4a4a;
    --navy-deep: #06183a;
    --navy: #0d2e66;
    --navy-glow: #1f5bb3;
    --paper: #eef0f2;
    --ink-light: #ffffff;
    --ink-soft: #d9e3f3;
    --rule: #7f9ccc;
  }
  * { box-sizing: border-box; margin: 0; padding: 0; }
  html, body { width: 1067px; height: 1200px; overflow: hidden; }
  body {
    background: var(--page-bg);
    font-family: "Questrial", "Helvetica Neue", Arial, sans-serif;
    position: relative;
  }
  .card {
    position: absolute;
    left: 103px;
    width: 860px;
    height: 490px;
    border-radius: 4px;
    overflow: hidden;
    box-shadow: 0 14px 34px rgba(0,0,0,.45);
  }

  /* Front */
  .card--front {
    top: 70px;
    background: radial-gradient(ellipse 60% 70% at 55% 30%, var(--navy-glow) 0%, var(--navy) 45%, var(--navy-deep) 100%);
    color: var(--ink-light);
  }
  .front-lockup {
    position: absolute;
    left: 110px; top: 150px;
    display: flex; align-items: center; gap: 22px;
  }
  .brand-square {
    width: 96px; height: 96px;
    border: 7px solid currentColor;
    flex: none;
  }
  .brand-text { display: flex; flex-direction: column; }
  .brand-name {
    font-size: 44px;
    letter-spacing: 3px;
    line-height: 1.08;
    text-transform: uppercase;
  }
  .brand-tagline {
    font-size: 15px;
    font-style: italic;
    letter-spacing: .3px;
    margin-top: 6px;
  }
  .front-url {
    position: absolute;
    left: 0; right: 0; top: 370px;
    text-align: center;
    font-size: 19px;
    letter-spacing: 1px;
    color: var(--ink-soft);
  }

  /* Back */
  .card--back {
    top: 630px;
    background: var(--paper);
  }
  .back-top {
    position: absolute; inset: 0 0 auto 0; height: 205px;
    color: var(--navy);
  }
  .back-top .front-lockup { left: 60px; top: 48px; }
  .back-top .brand-square { width: 84px; height: 84px; border-width: 6px; }
  .back-top .brand-name { font-size: 38px; }
  .back-top .brand-tagline { font-size: 14px; }
  .back-band {
    position: absolute; left: 0; right: 0; top: 205px; bottom: 0;
    background: radial-gradient(ellipse 55% 80% at 45% 0%, var(--navy-glow) 0%, var(--navy) 50%, var(--navy-deep) 100%);
    border-top: 8px solid var(--navy);
    box-shadow: 0 -4px 0 var(--paper), 0 -7px 0 var(--navy);
    color: var(--ink-light);
  }
  .contact-person {
    position: absolute; left: 70px; top: 110px;
  }
  .person-name { font-size: 26px; }
  .person-title { font-size: 17px; color: var(--ink-soft); margin-top: 4px; }
  .person-lines { margin-top: 22px; font-size: 18px; line-height: 1.45; }
  .contact-divider {
    position: absolute; left: 405px; top: 40px; height: 150px;
    border-left: 1px solid var(--rule);
  }
  .contact-company {
    position: absolute; left: 435px; top: 40px;
    font-size: 18px; line-height: 1.4;
  }
  .contact-company .gap { margin-top: 20px; }
</style>
</head>
<body>
  <section class="card card--front" aria-label="Card front">
    <div class="front-lockup">
      <span class="brand-square"></span>
      <div class="brand-text">
        <span class="brand-name">Keystride<br>Facility Services</span>
        <span class="brand-tagline">One Source For Landscape, Janitorial and Facility Maintenance</span>
      </div>
    </div>
    <p class="front-url">www.keystridefacilityservices.com</p>
  </section>

  <section class="card card--back" aria-label="Card back">
    <div class="back-top">
      <div class="front-lockup">
        <span class="brand-square"></span>
        <div class="brand-text">
          <span class="brand-name">Keystride<br>Facility Services</span>
          <span class="brand-tagline">One Source For Landscape, Janitorial and Facility Maintenance</span>
        </div>
      </div>
    </div>
    <div class="back-band">
      <div class="contact-person">
        <p class="person-name">Marcus Hale</p>
        <p class="person-title">General manager</p>
        <div class="person-lines">
          <p>p: +(00) 00 0000 0000</p>
          <p>f: +(00) 00 0000 0000</p>
        </div>
      </div>
      <span class="contact-divider"></span>
      <div class="contact-company">
        <p>Keystride Facility Center</p>
        <p>Cedar Bend, Fort Worth,</p>
        <p>keystridefacilityservices.com</p>
        <p class="gap">e: info@keystridefacilityservices.com</p>
        <p>w: www.keystridefacilityservices.com</p>
      </div>
    </div>
  </section>
</body>
</html>
```